We have over 30 years of experience in various construction projects. New additions, rehab work, interior and exterior etc. We started our own company about a year ago.
I am attaching a card that I received from a client that I really like and would like to follow as a template, but I am very open to your creative approach. I am interested in my logo (which will be later used for my website) to incorporate the "M&P" or "M&P Remodeling" Please email me at mpremodeling 81@brindlemail.com or call Walt at 773-555-0182.

Industry/Entity Type

Construction

Contact Information for Business Card

M&P Remodeling and Beacon Services
2816 W Oakridge Ave
Westbrook, IL 60799
708-555-0147 - Polish
708-555-0163 - English

Piotr Walek - Owner
Marek WAlek Jr - Construction Manager
mpremodeling81@brindlemail.com

```html
<!DOCTYPE html>
<html lang="en">
<head>
<meta charset="utf-8">
<title>M&amp;P Remodeling and Beacon Services — Business Card</title>
<link rel="stylesheet" href="https://fonts.googleapis.com/css2?family=Fira+Sans:wght@400;600&display=swap">
<style>
  :root {
    --page-bg-top: #f4f4f4;
    --page-bg-bottom: #d6d6d6;
    --card-bg: #1c1c1c;
    --card-bg-edge: #262626;
    --text-bright: #ececec;
    --text-soft: #b9b9b9;
    --text-dim: #6f6f6f;
    --rule: #8a8a8a;
    --skyline-light: #4a4a4a;
    --skyline-dark: #222222;
  }
  * { box-sizing: border-box; margin: 0; padding: 0; }
  html, body { width: 1200px; height: 1200px; overflow: hidden; }
  body {
    background: linear-gradient(180deg, var(--page-bg-top), var(--page-bg-bottom));
    font-family: "Fira Sans", sans-serif;
    display: flex;
    flex-direction: column;
    align-items: center;
    justify-content: center;
    gap: 70px;
  }
  .card {
    position: relative;
    width: 700px;
    height: 400px;
    background: radial-gradient(ellipse at 40% 40%, var(--card-bg-edge), var(--card-bg) 70%);
    box-shadow: 0 14px 30px rgba(0,0,0,0.25);
    overflow: hidden;
  }

  /* Front */
  .front .skyline-band {
    position: absolute;
    left: 0; right: 0;
    top: 90px; height: 150px;
    background: linear-gradient(180deg, transparent, var(--skyline-light) 85%, var(--skyline-dark));
    opacity: 0.7;
  }
  .front .horizon {
    position: absolute;
    left: 0; right: 0; top: 240px;
    height: 2px;
    background: linear-gradient(90deg, transparent, var(--rule), transparent);
  }
  .front .brand-mark {
    position: absolute;
    left: 0; right: 0; top: 150px;
    text-align: center;
    font-size: 72px;
    font-weight: 600;
    color: var(--text-bright);
    letter-spacing: 2px;
  }
  .front .brand-line {
    position: absolute;
    left: 0; right: 0; top: 262px;
    text-align: center;
    font-size: 26px;
    font-weight: 400;
    color: var(--text-dim);
    letter-spacing: 3px;
    text-transform: uppercase;
  }

  /* Back */
  .back .brand-mark {
    position: absolute;
    left: 40px; top: 36px;
    font-size: 56px;
    font-weight: 600;
    color: var(--text-soft);
  }
  .back .skyline-band {
    position: absolute;
    left: 260px; right: 0;
    top: 110px; height: 130px;
    background: linear-gradient(180deg, transparent, var(--skyline-light));
    -webkit-mask-image: linear-gradient(90deg, transparent, #000 40%);
    mask-image: linear-gradient(90deg, transparent, #000 40%);
    opacity: 0.45;
  }
  .back .person {
    position: absolute;
    right: 40px; top: 120px;
    text-align: left;
  }
  .back .person-name {
    font-size: 22px;
    font-weight: 600;
    color: var(--text-bright);
  }
  .back .person-role {
    font-size: 15px;
    color: var(--text-soft);
    line-height: 1.3;
  }
  .back .details {
    position: absolute;
    left: 40px; right: 40px; top: 255px;
    display: flex;
    gap: 22px;
  }
  .back .address {
    width: 210px;
    text-align: right;
    font-size: 17px;
    color: var(--text-soft);
    line-height: 1.35;
    padding-top: 4px;
  }
  .back .divider {
    width: 1px;
    background: var(--rule);
  }
  .back .contacts {
    display: flex;
    flex-direction: column;
    gap: 2px;
    font-size: 19px;
    color: var(--text-bright);
  }
  .back .contact-row {
    display: flex;
    align-items: center;
    gap: 10px;
  }
  .back .contact-row.indent { padding-left: 34px; }
  .back .icon {
    width: 24px; height: 24px;
    flex: none;
  }
</style>
</head>
<body>
  <section class="card front">
    <div class="skyline-band" role="img" aria-label="Outline drawing of a city skyline"></div>
    <div class="horizon"></div>
    <div class="brand-mark">M&amp;P</div>
    <div class="brand-line">Remodeling and Beacon Services</div>
  </section>

  <section class="card back">
    <div class="brand-mark">M&amp;P</div>
    <div class="skyline-band" role="img" aria-label="Faint outline drawing of city towers"></div>
    <div class="person">
      <div class="person-name">Piotr Walek</div>
      <div class="person-role">Owner Marek Walek Jr<br>Construction Manager</div>
    </div>
    <div class="details">
      <div class="address">2816 W Oakridge<br>Ave Westbrook, IL</div>
      <div class="divider"></div>
      <div class="contacts">
        <div class="contact-row">
          <svg class="icon" viewBox="0 0 24 24" aria-hidden="true">
            <rect width="24" height="24" rx="3" fill="#5a5a5a"/>
            <path d="M8 5 l3 3 -1.5 2 q1.5 3 4.5 4.5 l2 -1.5 3 3 -2 2 q-7 -1 -11 -11z" fill="#1c1c1c"/>
          </svg>
          <span>Polish : 60799 708-555-0147,</span>
        </div>
        <div class="contact-row indent"><span>English : 708-555-0163</span></div>
        <div class="contact-row">
          <svg class="icon" viewBox="0 0 24 24" aria-hidden="true">
            <rect width="24" height="24" rx="3" fill="#5a5a5a"/>
            <rect x="5" y="7" width="14" height="10" fill="#1c1c1c"/>
            <path d="M5 7 l7 6 7 -6" fill="none" stroke="#5a5a5a" stroke-width="1.5"/>
          </svg>
          <span>mpremodeling81@brindlemail.com</span>
        </div>
      </div>
    </div>
  </section>
</body>
</html>
```